依頼詳細
お客様と話をする際、代理店や営業マンがお客様にお見せして、瞬時にポイントがわかり、詳細まで見たくなる仕上がりにしたいと考えています。
記載項目
文字、文言は添付ファイルにでています。
記載したい文字や協調したい文言は、文字の大きさで表現していますので、参考
にしてください。
表面
配置や色使いはお任せ致します。ポイントが目に飛び込んでくる様な仕上げに
してください。
裏面
事例が4例でてます。ポイントは赤字にしてありますが、元の配置や文字ポイン
ト・色は無視
して頂いて結構です。ポイントがわかりやすい仕上がりでお願い致します。
グラフについても同様で、意味が同じであればどんな色でもOKです。

サイズ
A4
ページ数
両面
希望イメージ
シンプル 複雑
単色 カラフル
暗い 明るい
日常 高級
遊び心 厳粛
未来的 伝統的
女性的 男性的
希望する色
水色系、グレー系
納品ファイル
• イラストレーター形式 (.ai)
補足説明
構成やデザインについての変更は、ありませんが文字(数値)などの変更をお願いする事がありますので、その節には対応の程お願い致します。
ロゴは、aiファイルに貼ってあります。
■ 選んだ理由

本当に悩みましたが
今回の利用目的を考慮した結果です。

■ 提案者全員のお礼・コメント

本当に、迷いました。
また機会がございましたら、是非ご応募いただきます様お願い致します。
皆さま方の今後の活躍を期待しております。

```html
<!DOCTYPE html>
<html lang="ja">
<head>
<meta charset="utf-8">
<title>オフィスビルの削減事例 | ミナト電力</title>
<link href="https://fonts.googleapis.com/css2?family=M+PLUS+Rounded+1c:wght@500;700;800;900&display=swap" rel="stylesheet">
<style>
:root{
  --sky:#d9effa;
  --sky-deep:#9fd4f0;
  --green:#3f9a2e;
  --green-light:#7cc54a;
  --green-pale:#e6f4d7;
  --red:#e23a26;
  --salmon:#ee9a7c;
  --ink:#333;
  --white:#fff;
  --band:#f3fbe9;
}
*{margin:0;padding:0;box-sizing:border-box}
html,body{width:861px;height:1200px;overflow:hidden}
body{font-family:"M PLUS Rounded 1c",sans-serif;color:var(--ink);
  background:linear-gradient(180deg,var(--sky-deep) 0%,var(--sky) 18%,#f4fbff 60%,var(--sky) 100%);position:relative}
.flyer{position:absolute;inset:0}
.title{position:absolute;left:0;top:14px;width:100%;text-align:center;font-weight:900;font-size:38px;color:var(--green);letter-spacing:1px;
  text-shadow:0 2px 0 var(--white),0 -2px 0 var(--white),2px 0 0 var(--white),-2px 0 0 var(--white)}
.section-head{position:absolute;left:18px;width:825px;height:42px;border-radius:6px;
  background:linear-gradient(90deg,var(--white),var(--band) 60%,transparent);
  font-weight:900;font-size:29px;color:var(--green);padding-left:14px;line-height:42px}
.chart{position:absolute}
.tag{position:absolute;background:var(--green-light);color:var(--white);font-weight:800;font-size:16px;padding:3px 10px;border-radius:4px}
.note{position:absolute;font-size:13px;font-weight:700;line-height:1.35}
.saving{position:absolute;background:var(--salmon);border-radius:48% 52% 46% 54%/55% 55% 45% 45%;
  color:var(--white);font-weight:900;display:flex;flex-direction:column;align-items:center;justify-content:center;text-align:center;line-height:1.05}
.saving .small{font-size:18px;font-weight:800}
.saving .big{font-size:52px}
.saving .mid{font-size:30px}
.figure{position:absolute;background:linear-gradient(180deg,#f6e2cf,#c9d8e6);border-radius:20px}
.caption{position:absolute;font-size:12px;font-weight:700;color:#555}
.rental{position:absolute;left:0;top:1028px;width:100%;text-align:center;font-weight:900;font-size:24px;color:var(--green)}
.rental em{font-style:normal;color:var(--red);font-size:32px}
.footer{position:absolute;left:0;top:1070px;width:100%;height:130px;background:var(--white)}
.free{position:absolute;left:28px;top:12px;background:var(--red);color:var(--white);font-weight:800;font-size:18px;padding:3px 14px;border-radius:4px}
.tel{position:absolute;left:28px;top:42px;font-weight:900;font-size:34px;color:var(--green)}
.brand{position:absolute;left:28px;top:88px;font-weight:800;font-size:26px;color:var(--ink)}
.stamp-box{position:absolute;left:472px;top:14px;width:365px;height:104px;border:2px solid var(--sky-deep);border-radius:6px}
</style>
</head>
<body>
<div class="flyer">
  <h1 class="title">こんなに変わる！オフィスビルの削減事例</h1>

  <h2 class="section-head" style="top:74px">LED交換による削減例</h2>
  <svg class="chart" style="left:22px;top:124px" width="400" height="276" viewBox="0 0 400 276">
    <rect x="0" y="0" width="400" height="276" rx="8" fill="#e6f4d7"/>
    <g font-family="M PLUS Rounded 1c, sans-serif" font-weight="800">
      <text x="100" y="22" font-size="14" text-anchor="middle" fill="#333">蛍光灯 (ベースライト)</text>
      <text x="300" y="22" font-size="14" text-anchor="middle" fill="#333">白熱球 (ダウンライト)</text>
      <rect x="18" y="70" width="70" height="170" fill="#3f9a2e"/>
      <text x="53" y="170" font-size="28" text-anchor="middle" fill="#fff">40W</text>
      <rect x="118" y="160" width="70" height="80" fill="#7cc54a"/>
      <text x="153" y="208" font-size="26" text-anchor="middle" fill="#fff">19W</text>
      <rect x="218" y="70" width="70" height="170" fill="#3f9a2e"/>
      <text x="253" y="170" font-size="28" text-anchor="middle" fill="#fff">60W</text>
      <rect x="318" y="210" width="70" height="30" fill="#7cc54a"/>
      <text x="353" y="202" font-size="24" text-anchor="middle" fill="#3f9a2e">6W</text>
      <path d="M90 50 L115 140 L104 140 L126 165 L136 135 L125 137 L100 46 Z" fill="#e23a26"/>
      <text x="120" y="85" font-size="22" fill="#e23a26">約1/2</text>
      <path d="M290 50 L315 180 L304 180 L326 205 L336 175 L325 177 L300 46 Z" fill="#e23a26"/>
      <text x="325" y="100" font-size="26" fill="#e23a26">1/10</text>
      <g font-size="11" fill="#555" font-weight="700" text-anchor="middle">
        <text x="53" y="260">40W相当品</text><text x="153" y="260">LED蛍光灯</text>
        <text x="253" y="260">60W相当品</text><text x="353" y="260">LED電球</text>
      </g>
    </g>
  </svg>
  <div class="tag" style="left:432px;top:140px">LED導入前</div>
  <div class="note" style="left:432px;top:172px">消費電力 55,836kWh<br>電気料金<b style="color:var(--red);font-size:17px">121万円</b></div>
  <div class="tag" style="left:432px;top:260px">LED導入後</div>
  <div class="note" style="left:432px;top:292px">消費電力 17,702kWh<br>電気料金<b style="color:var(--red);font-size:17px">38万円</b></div>
  <div class="saving" role="img" aria-label="豚の貯金箱のイラスト（削減額）" style="left:590px;top:150px;width:250px;height:200px">
    <span class="big">87万円</span><span class="mid">削減！</span>
  </div>
  <div class="caption" style="left:630px;top:360px">電気料金は年間の試算</div>

  <h2 class="section-head" style="top:406px">電気料金見直しによる削減例</h2>
  <svg class="chart" style="left:22px;top:456px" width="360" height="250" viewBox="0 0 360 250">
    <rect width="360" height="250" rx="8" fill="#e6f4d7"/>
    <g font-family="M PLUS Rounded 1c, sans-serif" font-weight="800">
      <text x="90" y="24" font-size="15" text-anchor="middle" fill="#333">ミナト電力</text>
      <text x="90" y="44" font-size="17" text-anchor="middle" fill="#e23a26">切り替え前</text>
      <text x="90" y="62" font-size="12" text-anchor="middle" fill="#555">の電気料金</text>
      <text x="270" y="24" font-size="15" text-anchor="middle" fill="#333">ミナト電力</text>
      <text x="270" y="44" font-size="17" text-anchor="middle" fill="#e23a26">切り替え後</text>
      <text x="270" y="62" font-size="12" text-anchor="middle" fill="#555">の電気料金</text>
      <rect x="30" y="80" width="120" height="160" fill="#3f9a2e"/>
      <text x="90" y="200" font-size="30" text-anchor="middle" fill="#fff">999<tspan font-size="16">万円</tspan></text>
      <rect x="210" y="100" width="120" height="140" fill="#7cc54a"/>
      <text x="270" y="200" font-size="30" text-anchor="middle" fill="#fff">879<tspan font-size="16">万円</tspan></text>
      <path d="M150 78 L195 115 L187 121 L214 128 L206 101 L200 108 L156 70 Z" fill="#e23a26"/>
      <text x="182" y="92" font-size="16" fill="#e23a26">約</text>
      <text x="172" y="150" font-size="22" fill="#e23a26">12%</text>
      <text x="180" y="168" font-size="14" fill="#e23a26">削減</text>
    </g>
  </svg>
  <div class="figure" role="img" aria-label="スーツ姿の男女が説明するイラスト" style="left:398px;top:470px;width:170px;height:230px"></div>
  <div class="saving" role="img" aria-label="豚の貯金箱のイラスト（削減額）" style="left:590px;top:480px;width:250px;height:200px">
    <span class="small">約12%削減</span><span class="big">120万円</span><span class="mid">削減！</span>
  </div>
  <div class="caption" style="left:630px;top:690px">電気料金は年間の試算</div>

  <h2 class="section-head" style="top:722px">LED＋新電力のセットがお得</h2>
  <svg class="chart" style="left:22px;top:772px" width="540" height="250" viewBox="0 0 540 250">
    <rect width="540" height="250" rx="8" fill="#e6f4d7"/>
    <g font-family="M PLUS Rounded 1c, sans-serif" font-weight="800">
      <rect x="30" y="50" width="120" height="170" fill="#3f9a2e"/>
      <text x="90" y="130" font-size="20" text-anchor="middle" fill="#fff">年間</text>
      <text x="90" y="170" font-size="34" text-anchor="middle" fill="#fff">999</text>
      <text x="90" y="196" font-size="18" text-anchor="middle" fill="#fff">万円</text>
      <rect x="210" y="74" width="120" height="146" fill="#5db23a"/>
      <text x="270" y="140" font-size="20" text-anchor="middle" fill="#fff">年間</text>
      <text x="270" y="178" font-size="34" text-anchor="middle" fill="#fff">879</text>
      <text x="270" y="202" font-size="18" text-anchor="middle" fill="#fff">万円</text>
      <rect x="390" y="92" width="120" height="128" fill="#7cc54a"/>
      <text x="450" y="150" font-size="20" text-anchor="middle" fill="#fff">年間</text>
      <text x="450" y="186" font-size="34" text-anchor="middle" fill="#fff">792</text>
      <text x="450" y="208" font-size="18" text-anchor="middle" fill="#fff">万円</text>
      <rect x="190" y="10" width="150" height="28" rx="4" fill="#fff"/>
      <text x="265" y="31" font-size="19" text-anchor="middle" fill="#e23a26">120万円削減！</text>
      <rect x="370" y="10" width="160" height="28" rx="4" fill="#fff"/>
      <text x="450" y="31" font-size="19" text-anchor="middle" fill="#e23a26">207万円削減！</text>
      <path d="M150 56 L200 66 L198 58 L212 72 L196 84 L198 76 L150 66 Z" fill="#e23a26"/>
      <path d="M330 80 L380 90 L378 82 L392 96 L376 108 L378 100 L330 90 Z" fill="#e23a26"/>
      <g font-size="12" fill="#555" font-weight="700" text-anchor="middle">
        <text x="90" y="238">現行 電気料金</text><text x="270" y="238">新電力 電気料金</text><text x="450" y="238">新電力+LED 電気料金</text>
      </g>
    </g>
  </svg>
  <div class="saving" role="img" aria-label="豚の貯金箱のイラスト（投資回収）" style="left:580px;top:790px;width:260px;height:200px">
    <span class="small">導入費用</span><span class="mid" style="font-size:38px">578万円</span><span class="small">投資回数</span><span class="mid" style="font-size:38px">2.8年</span>
  </div>
  <div class="caption" style="left:615px;top:998px">さらに環境貢献の効果!!</div>

  <p class="rental">ミナト電力レンタルを利用することで、導入費用はなんと<em>０円</em>！</p>

  <footer class="footer">
    <div class="free">お見積もりは無料です！</div>
    <div class="tel">TEL.03-4321-8765</div>
    <div class="brand">ミナト電力</div>
    <div class="stamp-box"></div>
  </footer>
</div>
</body>
</html>
```